Talented energy healer needs business card design

I need a business card design for a new energy healing business in Perth Australia. As an energy healer I am quite earthy and practical rather than floaty and fairydust.
One of the techniques I use is unique in Australia but used internationally (US, UK and Europe). I practice with Coastal Pathway Method, Reiki and massage as well as some other techniques I developed personally. I am starting to incorporate sound healing into my practice. I literally change people's lives. The potential for each client is wide open. A key skill I bring to my practice is the capacity for making difficult situations seem more fun and less stressful.
Clients are likely to be depressed, physically unwell, going through a difficult time, unhappy with their current situation. They are people looking for new options to solve a difficult existing problem. They have probably tried other avenues before they come to me. They are open to something different.

I would like to communicate that the client and I work together for their healing and personal growth. I would like to convey that while the work of changing is challenging it can also be fun.
Updates

Hi all, info required on the card is:

Name
Title: Healer
contact number (mobile)
I don''t have a logo - I would be interested in seeing designs that use the whole card as well as the traditional logo on one side / in one corner. Whatever ''look/feel'' I choose will carry over to the website as well.

thanks
Meg

Reason: One or two of the designs caught my eye and many appeal for different reasons, but nothing is quite right for me. I've invited a couple of other designers to contribute so I wanted to give them time to be involved. kind regards Meg

Thank you all for the fabulous designs. I really appreciated the thought that many people put into my brief and a number of designs captured important things about what I was trying to say. It was a hard choice between 3 designs in the end.
thanks again and kind regards
Meg

Target Market(s)

people looking for new options to solve a difficult existing problem

Industry/Entity Type

Massage

Logo styles of interest
Abstract Logo
Requirements
Must have
• include green and blue
Nice to have
• hands, tea / teapots , the ocean, stepping stones

```html
<!DOCTYPE html>
<html lang="en">
<head>
<meta charset="utf-8">
<title>Healer Business Card</title>
<link rel="stylesheet" href="https://fonts.googleapis.com/css2?family=Open+Sans:wght@300;400;700&display=swap">
<style>
  :root {
    --page: #fffcfc;
    --card: #ffffff;
    --border: #111111;
    --orange: #f68b22;
    --accent-red: #e8472a;
    --leaf-green: #6fae4f;
    --ocean-blue: #2f7fc1;
    --ink: #333333;
    --white: #ffffff;
  }
  html, body {
    margin: 0;
    padding: 0;
    width: 1200px;
    height: 2199px;
    overflow: hidden;
    background: var(--page);
    font-family: "Open Sans", sans-serif;
  }
  .canvas {
    position: relative;
    width: 1200px;
    height: 2199px;
  }
  .card {
    position: absolute;
    left: 80px;
    top: 200px;
    width: 1039px;
    height: 1799px;
    box-sizing: border-box;
    border: 3px solid var(--border);
    background: var(--card);
  }
  .rules {
    position: absolute;
    inset: 0;
  }
  .rules line, .rules polyline {
    stroke: var(--orange);
    stroke-width: 3;
    fill: none;
  }
  .name-tag {
    position: absolute;
    left: 631px;
    top: 311px;
    width: 447px;
    height: 153px;
    background: var(--orange);
    color: var(--white);
    text-align: right;
    box-sizing: border-box;
    padding: 18px 25px 0 0;
  }
  .name-tag .person {
    font-weight: 700;
    font-size: 44px;
    line-height: 58px;
  }
  .name-tag .role {
    font-weight: 400;
    font-size: 44px;
    line-height: 58px;
  }
  .brand {
    position: absolute;
    left: 262px;
    top: 711px;
    width: 635px;
    height: 440px;
    display: flex;
    align-items: center;
    justify-content: center;
    gap: 24px;
  }
  .brand .dot {
    width: 64px;
    height: 64px;
    border-radius: 50%;
    background: var(--ocean-blue);
  }
  .brand .brand-name {
    font-size: 72px;
    font-weight: 400;
    color: var(--leaf-green);
  }
  .email-handle {
    position: absolute;
    left: 340px;
    top: 1172px;
    width: 200px;
    text-align: center;
    font-size: 40px;
    line-height: 56px;
    color: var(--accent-red);
  }
  .contact {
    position: absolute;
    left: 150px;
    top: 1658px;
    width: 903px;
    text-align: right;
    color: var(--ink);
    font-size: 44px;
    line-height: 59px;
    font-weight: 400;
  }
  .contact p { margin: 0; }
  .contact .label { color: var(--ocean-blue); }
</style>
</head>
<body>
<div class="canvas">
  <div class="card"></div>

  <svg class="rules" width="1200" height="2199" viewBox="0 0 1200 2199" aria-hidden="true">
    <line x1="631" y1="464" x2="631" y2="650"/>
    <line x1="80" y1="650" x2="1119" y2="650"/>
    <line x1="80" y1="663" x2="1119" y2="663"/>
    <polyline points="154,663 154,1227 941,1227 941,1610 257,1610"/>
    <polyline points="315,689 176,689 176,1200 315,1200"/>
    <polyline points="537,1200 973,1200 973,1642 1076,1642 1076,1951 973,1951"/>
    <polyline points="257,1642 154,1642 154,1951 257,1951"/>
  </svg>

  <div class="name-tag">
    <div class="person">Meg Harlow</div>
    <div class="role">Healer</div>
  </div>

  <div class="brand">
    <span class="dot"></span>
    <span class="brand-name">Tidewell</span>
  </div>

  <div class="email-handle">meg@</div>

  <div class="contact">
    <p>Coastal Pathway Method, Reiki, Massage</p>
    <p>Perth, Australia <span class="label">Mobile</span> :+61 (412) 88 88</p>
    <p><span class="label">Phone</span> :+61 (877) 77 77</p>
    <p><span class="label">E-Mail</span> :meg@tidewell.com</p>
  </div>
</div>
</body>
</html>
```